Poster for a Bicycle show/Expo

We need a poster for a Bicycle show/Expo and sustainable transport. Exhibitors will sell bikes, cycling clothing, accessories, etc. ...
This show is annual and the Poster is for the 2016 edition.

Your concept must be compatible in a landscape format. (We will ourselves adaptations of different formats.)
Width: 210 mm
Height: 297 mm
It's necessary for us to have the source file (vector) for make, later, the different format (flyers, website, ...)

Content of the Poster:
- 1 big picture (one of the two attached)
- Big title (typo-title worked): « Foire du Rouet » (« Salon » or « Salon du » can be small and « Vélo » big.)
- Subtitle: « et de la mobilité durable »
- Date: « 18, 19 et 20 mars 2016 » or « 18-20 mars 2016 »
- Place: « Halle RTP - Gare de Plantaz »
- Text line 1: « www.foire-du-rouet.ch »
- Text line 2: « Entrée gratuite »
- Text line 3: « Ve 18 mars de 17h à 20h - Sa 19 mars de 10h à 18h - Di 20 mars de 10h à 17h »
- Please, leave a zone in the poster for sponsors logos
(The predominant information (most visible) are: « Vélo » and « 18, 19 et 20 mars 2016 » or « 18-20 mars 2016 »)

Target Market(s)

Bicycle fan

Industry/Entity Type

Sporting Good

Font styles to use
Serif
Sans Serif

Colors
add136
ffffff
ec1f27

Requirements
Must have
• The style must be modern, dynamic, bright colors.

```html
<!DOCTYPE html>
<html lang="fr">
<head>
<meta charset="utf-8">
<title>Foire du Rouet 2016</title>
<link rel="stylesheet" href="https://fonts.googleapis.com/css2?family=Nunito:wght@700;800;900&family=Roboto+Condensed:wght@400;700&display=swap">
<style>
  :root {
    --red: #ec1f27;
    --green: #add136;
    --white: #ffffff;
    --navy: #1b2f6b;
    --sky-top: #0a3f9a;
    --sky-mid: #3b86d6;
    --sky-low: #bfe2f6;
    --hill-dark: #5e9e1e;
    --hill-light: #a9d63c;
    --grey: #9a9a9a;
  }
  * { margin: 0; padding: 0; box-sizing: border-box; }
  html, body { width: 849px; height: 1200px; overflow: hidden; background: var(--white); }
  .poster { position: relative; width: 849px; height: 1200px; overflow: hidden; font-family: "Nunito", sans-serif; }
  .scene { position: absolute; inset: 0; }
  .header { position: absolute; top: 40px; left: 0; width: 100%; text-align: center; }
  .title-small { font-size: 80px; font-weight: 900; color: var(--red); line-height: 1;
    text-shadow: 0 0 2px var(--white), 2px 2px 0 var(--white), -2px -2px 0 var(--white), 2px -2px 0 var(--white), -2px 2px 0 var(--white); }
  .title-big { font-size: 200px; font-weight: 900; color: var(--red); line-height: 0.95; letter-spacing: -4px;
    text-shadow: 4px 4px 0 var(--white), -3px -3px 0 var(--white), 3px -3px 0 var(--white), -3px 3px 0 var(--white); }
  .subtitle { margin-top: 18px; font-family: "Roboto Condensed", sans-serif; font-size: 34px; color: var(--navy); }
  .date { font-size: 58px; font-weight: 900; color: var(--red); line-height: 1.05; }
  .place { font-family: "Roboto Condensed", sans-serif; font-weight: 700; font-size: 38px; color: var(--navy); }
  .banner { position: absolute; left: -20px; background: var(--green); transform: rotate(-8deg); transform-origin: left top; padding-left: 50px; }
  .banner-info { top: 600px; width: 380px; height: 145px; padding-top: 22px; }
  .banner-info .web { font-family: "Roboto Condensed", sans-serif; font-weight: 700; font-size: 32px; color: var(--white); }
  .banner-info .free { font-family: "Roboto Condensed", sans-serif; font-weight: 700; font-size: 34px; color: var(--red); }
  .banner-hours { top: 775px; width: 330px; height: 135px; padding: 16px 14px 0 50px; font-family: "Roboto Condensed", sans-serif; font-size: 24px; line-height: 1.3; color: var(--white); }
  .sponsor { position: absolute; left: 0; top: 1145px; width: 600px; text-align: center; font-family: "Roboto Condensed", sans-serif; font-size: 28px; color: var(--grey); }
</style>
</head>
<body>
<div class="poster">
  <svg class="scene" width="849" height="1200" viewBox="0 0 849 1200" role="img" aria-label="Photo: a cyclist with a backpack standing by her bike on a green grassy hill under a blue sky">
    <defs>
      <linearGradient id="sky" x1="0" y1="0" x2="0" y2="1">
        <stop offset="0" stop-color="var(--sky-top)"/>
        <stop offset="0.55" stop-color="var(--sky-mid)"/>
        <stop offset="1" stop-color="var(--sky-low)"/>
      </linearGradient>
      <linearGradient id="hill" x1="0" y1="0" x2="0" y2="1">
        <stop offset="0" stop-color="var(--hill-light)"/>
        <stop offset="1" stop-color="var(--hill-dark)"/>
      </linearGradient>
    </defs>
    <rect width="849" height="1000" fill="url(#sky)"/>
    <path d="M0 880 C 250 860, 600 880, 849 925 L 849 1060 L 0 1060 Z" fill="url(#hill)"/>
    <path d="M0 1010 C 250 960, 550 1010, 849 975 L 849 1200 L 0 1200 Z" fill="var(--white)"/>
    <path d="M0 1010 C 250 960, 550 1010, 849 975" fill="none" stroke="var(--red)" stroke-width="6"/>
  </svg>

  <header class="header">
    <div class="title-small">Foire du</div>
    <div class="title-big">Rouet</div>
    <div class="subtitle">et de la mobilité durable</div>
    <div class="date">18, 19 et 20 mars 2016</div>
    <div class="place">Halle RTP - Gare de Plantaz</div>
  </header>

  <div class="banner banner-info">
    <div class="web">www.foire-du-rouet.ch</div>
    <div class="free">Entrée gratuite</div>
  </div>

  <div class="banner banner-hours">
    Ve 18 mars de 17h à 20h - Sa 19 mars de 10h à 18h - Di 20 mars de 10h à 17h
  </div>

  <div class="sponsor">for sponsor</div>
</div>
</body>
</html>
```